Design the New 3D Printing Database - MeshLocker.net

We’re hiring a designer to create a modern, intuitive, and scalable frontend design for MeshLocker.net — a search engine and aggregator for free 3D printable files (STL files).

The site will not host files, but will crawl and display listings from other 3D file platforms like Plankora, Buildwisp, and OurTinyForgeworks. We need a design that looks clean, tech-forward, and makes it easy for users to browse, search, and explore curated 3D print models.

Project Goals
• Help users search, filter, and browse STL files from various sources
• Present file listings in a clean and organized card-style layout
• Include strong category navigation, tag filtering, and search UX
• Allow for expansion — community features, user accounts, ads, etc.
• Be ready for handoff to developers

Pages & Components to Design

1. Homepage
• Featured models / Trending prints
• Search bar with predictive text
• Top categories (e.g., Tools, Toys, Miniatures, Cosplay)
• Optional: promo ad slot or “Featured Site of the Week”

2. Search Results Page
• Search bar at top
• Grid or list view of STL listings
• Filters on sidebar (category, tag, source site, popularity)
• Sort options (Newest, Most Viewed, Top Rated)

3. Individual File Listing Page
• Model thumbnail (placeholder for external image)
• Title, description, tags
• Source website badge/logo
• Button: “View on [Source Site]”
• Optional: 3D viewer embed (room for iframe or canvas)

4. Category Pages
• Header with category name and short description
• Grid of listings in that category

5. About / FAQ / Submit a File
• Basic static content page layout
• Contact form or submission form mockup

6. Admin Preview (Optional)
• Just 1-2 styled screens for how backend editing might look (not functional)

Design Requirements
• Responsive (desktop, tablet, mobile)
• Clean, modern UI (think: Web3 simplicity, Zentavo-level UX)
• Easy-to-read typography and smart use of whitespace
• Icons or badges for source platforms (e.g., Plankora, Buildwisp)
• Room for advertising placements (sidebar, inline, or homepage)

Style Inspiration
• Hero inspiration: FabScoutly.net — but cleaner
• Other ideas: Quillo Commons, Brivvells
• Optional: light/dark mode theme toggle

Deliverables
• Complete desktop and mobile Figma designs
• Style guide (colors, fonts, components)
• Assets and UI kit for development handoff
• Optionally, clickable prototype for demonstration

Target Market(s)

3D Printing Enthusiasts

Industry/Entity Type

3D Printing, Design, Engineering

Number of Pages Required

5+ page

Font styles to use
Sans Serif

```html
<!DOCTYPE html>
<html lang="en">
<head>
<meta charset="utf-8">
<title>MeshLocker.net — Free 3D Printable Models</title>
<link href="https://fonts.googleapis.com/css2?family=Outfit:wght@400;500;600;700&display=swap" rel="stylesheet">
<style>
:root{
  --teal:#17a7b5;
  --teal-soft:#e3f5f7;
  --ink:#1d2126;
  --muted:#5b636b;
  --line:#d9dee2;
  --page:#f4f7f8;
  --band:#eaeef0;
  --white:#ffffff;
  --violet-soft:#ece9fb;
  --violet:#6a5bd6;
}
*{box-sizing:border-box;margin:0;padding:0}
html,body{width:1200px;height:4115px;overflow:hidden}
body{position:relative;background:var(--page);font-family:"Outfit",sans-serif;color:var(--ink)}
.abs{position:absolute}
.header{position:absolute;left:0;top:0;width:1200px;height:133px;background:var(--white)}
.brand{font-weight:700;font-size:20px;color:var(--ink)}
.contact{display:flex;align-items:center;gap:8px;font-size:10px;font-weight:500}
.dot{width:22px;height:22px;border-radius:50%;background:var(--teal);display:flex;align-items:center;justify-content:center}
.nav a{position:absolute;top:82px;font-size:14px;color:var(--ink);text-decoration:none}
.search-mini{left:869px;top:72px;width:241px;height:40px;border:1px solid var(--line);border-radius:20px;padding:0 22px;display:flex;align-items:center;justify-content:space-between;font-size:13px;color:#8a9096;background:var(--white)}
.photo{border-radius:10px}
.hero-card{left:485px;top:395px;width:595px;height:362px;background:var(--white);border-radius:6px;box-shadow:0 10px 30px rgba(0,0,0,.08);padding:26px 40px}
.hero-card h1{font-size:37px;line-height:46px;font-weight:600;width:420px}
.hero-card p{margin-top:18px;font-size:13.5px;line-height:20px;width:420px}
.searchbar{display:flex;margin-top:22px;margin-left:-13px;height:40px}
.searchbar .field{flex:0 0 392px;border:1px solid var(--line);border-radius:20px 0 0 20px;padding:0 14px;display:flex;align-items:center;font-size:13px;color:#8a9096}
.btn-teal{background:var(--teal);color:var(--white);border-radius:22px;display:flex;align-items:center;justify-content:center;gap:8px;font-size:14px;font-weight:500}
.chips{display:flex;gap:8px;margin-top:12px;margin-left:-13px}
.chip{border:1px solid var(--line);border-radius:20px;height:38px;padding:0 21px;display:flex;align-items:center;font-size:13.5px;color:var(--muted)}
.circle-btn{width:54px;height:54px;border-radius:50%;border:1.5px solid #9aa1a7;display:flex;align-items:center;justify-content:center;background:transparent}
.section-title{font-size:35px;font-weight:600}
.cat{position:absolute;top:940px;width:120px;margin-left:-60px;text-align:center;font-size:14px}
.cat .icon{width:56px;height:56px;margin:8px auto 18px;border-radius:12px}
.cat.active .ring{width:88px;height:88px;border-radius:50%;border:3px solid #c6e9ee;margin:-8px auto 4px;display:flex;align-items:center;justify-content:center}
.cat.active .ring span{width:78px;height:78px;border-radius:50%;background:var(--teal);display:block}
.social-band{left:82px;top:1234px;width:1028px;height:81px;background:var(--band);border-radius:4px}
.soc{position:absolute;top:1259px;display:flex;align-items:center;gap:10px;font-size:9px;color:var(--muted)}
.soc i{width:30px;height:30px;border-radius:50%;background:var(--white);display:block}
.card{position:absolute;background:var(--white);border-radius:6px;box-shadow:0 10px 30px rgba(0,0,0,.07)}
.card h3{font-size:19px;font-weight:600}
.card .src{font-size:13px;margin-top:6px}
.card .src b{font-weight:600}
.tags{display:flex;gap:6px;margin-top:10px}
.tag{border:1px solid var(--line);border-radius:14px;height:26px;padding:0 18px;display:flex;align-items:center;font-size:10px;color:var(--muted)}
.view{display:inline-flex;align-items:center;height:34px;padding:0 24px;border-radius:18px;font-size:13.5px;margin-top:14px}
.view.teal{background:var(--teal-soft);color:var(--teal)}
.view.violet{background:var(--violet-soft);color:var(--violet)}
.band{left:0;top:2318px;width:1200px;height:503px;background:var(--band)}
.banner{left:85px;top:3150px;width:1027px;height:180px;border-radius:8px;background:linear-gradient(90deg,#9a8070 0%,#6f8e9a 25%,#6f8c97 60%,#8aa0ab 100%);overflow:hidden}
.footer{left:0;top:3877px;width:1200px;height:238px;background:var(--white)}
.flink{position:absolute;top:3984px;font-size:15px}
</style>
</head>
<body>

<header class="header">
  <div class="abs brand" style="left:85px;top:22px">MeshLocker.net</div>
  <div class="abs contact" style="left:714px;top:19px">
    <span class="dot"><svg width="11" height="11" viewBox="0 0 24 24"><path fill="#fff" d="M6.6 10.8a15.1 15.1 0 006.6 6.6l2.2-2.2c.3-.3.7-.4 1-.2 1.1.4 2.3.6 3.6.6.6 0 1 .4 1 1V20c0 .6-.4 1-1 1A17 17 0 013 4c0-.6.4-1 1-1h3.5c.6 0 1 .4 1 1 0 1.3.2 2.5.6 3.6.1.3 0 .7-.2 1z"/></svg></span>(555)010-246
  </div>
  <div class="abs contact" style="left:829px;top:19px">
    <span class="dot"><svg width="11" height="11" viewBox="0 0 24 24"><path fill="#fff" d="M3 6h18v12H3z"/><path d="M3 6l9 7 9-7" stroke="#17a7b5" stroke-width="2" fill="none"/></svg></span>hello@meshlocker.net
  </div>
  <div class="abs contact" style="left:994px;top:19px;color:var(--muted)">
    <span class="dot" style="background:#e6e9ec"></span>Login
    <span style="width:1px;height:16px;background:var(--ink);margin:0 6px"></span>Register
  </div>
  <div class="abs" style="left:83px;top:57px;width:1030px;height:2px;background:#b9bfc4"></div>
  <nav class="nav">
    <a style="left:80px">Home</a><a style="left:161px">Categories</a><a style="left:276px">Popular</a><a style="left:369px">Submit a File</a><a style="left:495px">About</a>
  </nav>
  <div class="abs search-mini">Search here...
    <svg width="14" height="14" viewBox="0 0 24 24"><circle cx="10" cy="10" r="7" stroke="#1d2126" stroke-width="3" fill="none"/><path d="M15 15l6 6" stroke="#1d2126" stroke-width="3"/></svg>
  </div>
</header>

<div class="abs photo" role="img" aria-label="Workshop scene with a 3D printer and a person holding a yellow printed part" style="left:83px;top:134px;width:1027px;height:527px;background:linear-gradient(100deg,#3a3d42 0%,#7c7f84 28%,#d7dadd 55%,#e9ebec 75%,#b7bcc0 100%)"></div>

<section class="abs hero-card">
  <h1>Discover &amp; Search Thousands of Free 3D Printable Models</h1>
  <p>Explore curated STL files from top platforms like Plankora, Buildwisp, and OurTinyForgeworks — all in one place.</p>
  <div class="searchbar">
    <div class="field">Search models, categories, tags...</div>
    <div class="btn-teal" style="flex:0 0 139px;margin-left:-1px">
      <svg width="13" height="13" viewBox="0 0 24 24"><circle cx="10" cy="10" r="7" stroke="#fff" stroke-width="3" fill="none"/><path d="M15 15l6 6" stroke="#fff" stroke-width="3"/></svg>Search
    </div>
  </div>
  <div class="chips">
    <span class="chip">Miniatures</span><span class="chip">Tools</span><span class="chip">Cosplay</span><span class="chip">Toys</span><span class="chip">Figurines</span>
  </div>
</section>

<div class="abs circle-btn" style="left:162px;top:703px"><svg width="18" height="12" viewBox="0 0 18 12"><path d="M17 6H2M6 1L1 6l5 5" stroke="#5b636b" stroke-width="1.5" fill="none"/></svg></div>
<div class="abs circle-btn" style="left:227px;top:703px"><svg width="18" height="12" viewBox="0 0 18 12"><path d="M1 6h15M12 1l5 5-5 5" stroke="#5b636b" stroke-width="1.5" fill="none"/></svg></div>

<h2 class="abs section-title" style="left:0;width:1185px;text-align:center;top:856px">Explore by Category</h2>
<div class="cat" style="left:237px"><div class="icon" role="img" aria-label="Toy blocks icon" style="background:linear-gradient(#e65b5b 0 40%,#f2c14e 40% 70%,#4aa3df 70%)"></div>Toys</div>
<div class="cat" style="left:341px"><div class="icon" role="img" aria-label="Miniature house icon" style="background:linear-gradient(#3f9ad6 0 40%,#e65b5b 40%)"></div>Miniatures</div>
<div class="cat" style="left:442px"><div class="icon" role="img" aria-label="Wrench and screwdriver icon" style="background:linear-gradient(135deg,#9aa3ab,#f2a33a)"></div>Tools</div>
<div class="cat active" style="left:546px"><div class="ring" role="img" aria-label="Cosplay icon, selected"><span></span></div>Cosplay</div>
<div class="cat" style="left:651px"><div class="icon" role="img" aria-label="Graduation cap icon" style="background:linear-gradient(#3a5a9a,#f0c24c)"></div>Educational</div>
<div class="cat" style="left:754px"><div class="icon" role="img" aria-label="Magic wand icon" style="background:linear-gradient(135deg,#f2c14e,#e6598b)"></div>Fantasy</div>
<div class="cat" style="left:850px"><div class="icon" role="img" aria-label="Paint palette icon" style="background:radial-gradient(circle,#f2a33a,#e65b5b)"></div>Art</div>
<div class="cat" style="left:957px"><div class="icon" role="img" aria-label="Gadget devices icon" style="background:linear-gradient(#3f9ad6,#f2c14e)"></div>Gadgets</div>
<div class="abs btn-teal" style="left:505px;top:1084px;width:190px;height:42px">View All Categories</div>

<div class="abs social-band"></div>
<div class="abs" style="left:152px;top:1274px;width:80px;height:1px;background:#cfd5d9"></div>
<div class="abs" style="left:970px;top:1274px;width:80px;height:1px;background:#cfd5d9"></div>
<div class="soc" style="left:262px"><i></i>Friendloop</div>
<div class="soc" style="left:388px"><i></i>Chirpline</div>
<div class="soc" style="left:502px"><i></i>Zentavo</div>
<div class="soc" style="left:617px"><i></i>Workweave</div>
<div class="soc" style="left:735px"><i style="background:#e8434a"></i>Clipstream</div>
<div class="soc" style="left:857px"><i></i>Snapgrid</div>

<h2 class="abs section-title" style="left:83px;top:1410px">Trending 3D Models</h2>

<div class="abs photo" role="img" aria-label="Painted multi-headed dragon miniature" style="left:86px;top:1475px;width:589px;height:615px;border-radius:4px;background:radial-gradient(ellipse at 45% 45%,#8a5a46 0%,#a9876f 35%,#e2dfdc 70%)"></div>
<article class="card" style="left:162px;top:1989px;width:440px;height:221px;padding:36px 40px">
  <h3>Posable Dragon Miniature</h3>
  <div class="src"><b>Source:</b> Buildwisp</div>
  <div class="tags"><span class="tag">Miniature</span><span class="tag">Fantasy</span><span class="tag">Articulated</span></div>
  <span class="view teal">View on Buildwisp</span>
</article>

<div class="abs" role="img" aria-label="Colourful plastic toy tools" style="left:707px;top:1475px;width:400px;height:237px;background:linear-gradient(90deg,#fff 0%,#f4f5f6 100%)">
  <div style="position:absolute;left:20px;top:18px;width:360px;height:190px;background:linear-gradient(90deg,#2452b8 0 16%,transparent 16% 24%,#e33 24% 42%,transparent 42% 52%,#f5c21c 52% 62%,transparent 62% 72%,#2b8ee0 72% 82%,transparent 82% 86%,#3bb54a 86%);opacity:.85;border-radius:6px"></div>
</div>
<article class="card" style="left:773px;top:1664px;width:278px;height:166px;padding:18px 22px">
  <h3 style="font-size:18px">Adjustable Wrench Tool</h3>
  <div class="src"><b>Source:</b> Plankora</div>
  <div class="tags"><span class="tag">Workshop</span><span class="tag">Tool</span></div>
  <span class="view violet">View on Plankora</span>
</article>

<div class="abs" role="img" aria-label="White and grey printed cosplay helmets" style="left:707px;top:1854px;width:400px;height:236px;background:linear-gradient(120deg,#c8a57a 0%,#b9b6b2 35%,#8a8c90 65%,#b79a72 100%)"></div>
<article class="card" style="left:746px;top:2045px;width:323px;height:165px;padding:18px 30px">
  <h3 style="font-size:18px">Star Warrior Cosplay Helmet</h3>
  <div class="src"><b>Source:</b> Buildwisp</div>
  <div class="tags"><span class="tag">Cosplay</span><span class="tag">Helmet</span></div>
  <span class="view teal">View on OurTinyForgeworks</span>
</article>

<div class="abs band"></div>
<div class="abs" style="left:218px;top:2408px;font-size:19px;font-weight:600">Modern Geometric Vase Set</div>
<div class="abs" style="left:218px;top:2436px;font-size:13px"><b style="font-weight:600">Source:</b> OurTinyForgeworks</div>
<div class="abs tags" style="left:520px;top:2411px;margin:0"><span class="tag">Workshop</span><span class="tag">Tool</span></div>
<span class="abs view teal" style="left:214px;top:2452px;background:#d9eef1">View on OurTinyForgeworks</span>
<div class="abs circle-btn" style="left:873px;top:2406px"><svg width="18" height="12" viewBox="0 0 18 12"><path d="M17 6H2M6 1L1 6l5 5" stroke="#5b636b" stroke-width="1.5" fill="none"/></svg></div>
<div class="abs circle-btn" style="left:938px;top:2406px"><svg width="18" height="12" viewBox="0 0 18 12"><path d="M1 6h15M12 1l5 5-5 5" stroke="#5b636b" stroke-width="1.5" fill="none"/></svg></div>
<div class="abs" style="left:240px;top:2985px;width:720px;height:80px;border-radius:50%;background:radial-gradient(ellipse,rgba(0,0,0,.16),rgba(0,0,0,0) 70%)"></div>
<div class="abs" style="left:200px;top:2539px;width:802px;height:437px;background:var(--white);border-radius:6px;padding:6px">
  <div role="img" aria-label="Three white geometric vases with flowers on a dark background" style="width:100%;height:100%;border-radius:4px;background:linear-gradient(180deg,#3e3f44 0%,#4a4b50 75%,#6a5c4e 82%,#4d4238 100%)"></div>
</div>

<section class="abs banner" role="img" aria-label="Banner photo of hands stacked together in teamwork">
  <div style="position:absolute;left:261px;top:52px;font-size:35px;font-weight:700;color:#fff">Featured Source Platform</div>
  <div style="position:absolute;left:261px;top:101px;width:360px;font-size:13px;line-height:19px;color:#fff">This week we're highlighting [Buildwisp.com], a go-to platform for high-quality STL files.</div>
  <div style="position:absolute;left:785px;top:66px;width:189px;height:42px;border-radius:21px;background:#fff;display:flex;align-items:center;justify-content:center;font-size:13.5px">Explore Buildwisp.com</div>
</section>

<h2 class="abs" style="left:190px;width:400px;top:3488px;text-align:center;font-size:31px;line-height:39px;font-weight:600">MeshLocker Community Coming Soon!</h2>
<p class="abs" style="left:210px;width:360px;top:3574px;text-align:center;font-size:13.5px;line-height:19px">Soon you'll be able to save favorites, rate models, and share your collections. Stay tuned.</p>
<div class="abs btn-teal" style="left:246px;top:3632px;width:124px;height:42px;font-size:13.5px">Join Waitlist</div>
<div class="abs" style="left:384px;top:3644px;font-size:14px">OR</div>
<div class="abs" style="left:419px;top:3632px;width:123px;height:42px;border-radius:21px;background:var(--teal-soft);color:var(--teal);display:flex;align-items:center;justify-content:center;font-size:13.5px">Get Notified</div>
<div class="abs circle-btn" style="left:335px;top:3717px"><svg width="18" height="12" viewBox="0 0 18 12"><path d="M17 6H2M6 1L1 6l5 5" stroke="#5b636b" stroke-width="1.5" fill="none"/></svg></div>
<div class="abs circle-btn" style="left:400px;top:3717px"><svg width="18" height="12" viewBox="0 0 18 12"><path d="M1 6h15M12 1l5 5-5 5" stroke="#5b636b" stroke-width="1.5" fill="none"/></svg></div>
<div class="abs photo" role="img" aria-label="Maker adjusting a resin 3D printer" style="left:667px;top:3434px;width:347px;height:384px;border-radius:12px;background:linear-gradient(120deg,#8d7a68 0%,#c9c3bc 45%,#e9e6e3 65%,#4aa8c9 80%,#e6e4e2 100%)"></div>

<footer class="abs footer">
  <div style="position:absolute;left:0;width:1250px;top:22px;text-align:center;font-size:35px;font-weight:600">MeshLocker.net</div>
  <div style="position:absolute;left:0;width:1250px;top:67px;text-align:center;font-size:13.5px">The smarter way to search STL files.</div>
</footer>
<span class="flink" style="left:333px">Home</span>
<span class="flink" style="left:409px">Categories</span>
<span class="flink" style="left:523px">Popular</span>
<span class="flink" style="left:611px">Submit a File</span>
<span class="flink" style="left:737px">About</span>
<span class="flink" style="left:815px">FAQ</span>
<span class="flink" style="left:877px">Contact</span>
<div class="abs" style="left:83px;top:4059px;width:1030px;height:1px;background:var(--line)"></div>
<div class="abs" style="left:83px;top:4085px;font-size:13px">© 2025 MeshLocker.net — Aggregating the 3D printing world.</div>
<div class="abs" style="left:884px;top:4086px;display:flex;gap:28px;font-size:11px;font-weight:500">
  <span>Friendloop</span><span>Chirpline</span><span>Workweave</span>
</div>
<div class="abs" style="left:1130px;top:4042px;width:40px;height:40px;border-radius:50%;background:var(--teal);display:flex;align-items:center;justify-content:center">
  <svg width="12" height="8" viewBox="0 0 12 8"><path d="M1 7l5-5 5 5" stroke="#fff" stroke-width="2" fill="none"/></svg>
</div>

</body>
</html>
```